I require a logo design and business card design.

The logo and business card is for a pre existing salon that I have purchased in the last 6 months. It is about to get a total facelift and so requires rebranding. It is currently very dated and only appeals to an older demographic, I'm hoping to keep existing clients but also encourage new and younger clients who will have more creative work done. The salon is in a seaside location, we have tourists as clients also. I would like the logo to reflect the creative nature of my business.
Target Market(s)
All ages, men and women. Middle to upper price demographic.
Industry/Entity Type
Business
Contact Information for Business Card
Logo on the front. Logo, address and phone number on the back.
Font styles to use
Colors
Designer to choose colors to be used in the design.
Requirements
Must have
- On the back of the card I also require 'next appointment details (date and time). As well as the salon name 'brightmoor hair design', the phone number 0251937428, and address 17 Wattlebank road Kelpie Bay.

Nice to have
- The salon has round mirrors, that could be part of a theme. It is also located in a coastal region, so that could be part of a theme.

Should not have
- Not too busy please

```html
<!DOCTYPE html>
<html lang="en">
<head>
<meta charset="utf-8">
<title>Brightmoor Hair Design – Business Card</title>
<link rel="stylesheet" href="https://fonts.googleapis.com/css2?family=Roboto:wght@400;500&display=swap">
<style>
  :root {
    --backdrop: #262626;
    --card-dark: #151515;
    --card-light: #ffffff;
    --ink-dark: #111111;
    --ink-light: #ffffff;
    --rule: #1a1a1a;
  }
  * { margin: 0; padding: 0; box-sizing: border-box; }
  html, body {
    width: 1200px;
    height: 1200px;
    overflow: hidden;
    background: var(--backdrop);
    font-family: "Roboto", Arial, sans-serif;
  }
  .canvas {
    width: 1200px;
    height: 1200px;
    display: flex;
    flex-direction: column;
    align-items: center;
    justify-content: center;
    gap: 56px;
  }
  .card {
    width: 900px;
    height: 514px;
    position: relative;
    box-shadow: 0 10px 30px rgba(0,0,0,0.45);
  }
  .card--front {
    background: var(--card-dark);
    display: flex;
    align-items: center;
    justify-content: center;
  }
  .card--back {
    background: var(--card-light);
    color: var(--ink-dark);
  }
  .brand {
    display: flex;
    align-items: center;
    gap: 16px;
    font-weight: 500;
    font-size: 44px;
    letter-spacing: 0.5px;
    white-space: nowrap;
  }
  .brand__dot {
    width: 22px;
    height: 22px;
    border-radius: 50%;
    background: currentColor;
    flex: none;
  }
  .card--front .brand { color: var(--ink-light); }
  .card--back .brand {
    position: absolute;
    top: 78px;
    left: 0;
    right: 0;
    justify-content: center;
    color: var(--ink-dark);
  }
  .appointment__title {
    position: absolute;
    top: 196px;
    left: 0;
    right: 0;
    text-align: center;
    font-size: 27px;
  }
  .field {
    position: absolute;
    display: flex;
    align-items: flex-end;
    font-size: 22px;
    white-space: nowrap;
  }
  .field__line {
    display: block;
    height: 0;
    border-bottom: 2px solid var(--rule);
    margin: 0 12px 6px;
  }
  .field--date { top: 250px; left: 70px; }
  .field--date .field__line { width: 500px; }
  .field--time { top: 300px; left: 440px; }
  .field--time .field__line { width: 280px; }
  .contact {
    position: absolute;
    top: 352px;
    left: 0;
    right: 0;
    text-align: center;
  }
  .contact__phone {
    font-size: 40px;
    letter-spacing: 1px;
  }
  .contact__address {
    margin-top: 6px;
    font-size: 26px;
  }
</style>
</head>
<body>
  <main class="canvas">
    <section class="card card--front" aria-label="Card front">
      <div class="brand"><span class="brand__dot"></span><span class="brand__name">Brightmoor Hair Design</span></div>
    </section>

    <section class="card card--back" aria-label="Card back">
      <div class="brand"><span class="brand__dot"></span><span class="brand__name">Brightmoor Hair Design</span></div>
      <p class="appointment__title">Your Next Appointment is</p>
      <div class="field field--date"><span>Date</span><span class="field__line"></span></div>
      <div class="field field--time"><span>Time</span><span class="field__line"></span><span>am/pm</span></div>
      <div class="contact">
        <p class="contact__phone">0251937428</p>
        <p class="contact__address">17 Wattlebank road Kelpie Bay.</p>
      </div>
    </section>
  </main>
</body>
</html>
```